DL Flyer for a Luggage & Backpack store

we need a flyer that we can use for expanding our business, we will use this for hotels, University and exciting customers, we need this to show what we stock, our USP and how to find us, a big factor is the WHY. it should also reflex our look and feel on our website mossharbour.com.au . There should also include room for a discount voucher. If you provide a great design we will get you to also complete a large decal design we need for the front of our store.

Business

• Please feel free to submit your own designs and not a rework of the one we have. Thanks

```html
<!DOCTYPE html>
<html lang="en">
<head>
<meta charset="utf-8">
<title>Moss Harbour – DL Flyer</title>
<link href="https://fonts.googleapis.com/css2?family=Montserrat:wght@400;500;600;700;800&family=Kaushan+Script&family=Amatic+SC:wght@700&family=Alfa+Slab+One&display=swap" rel="stylesheet">
<style>
:root{
  --navy:#1b3459;
  --yellow:#f7ec1a;
  --teal:#43c2a0;
  --teal-dark:#1f5d52;
  --ink:#1d1d1d;
  --white:#ffffff;
  --paper:#e9e5de;
  --grey:#5a5a5a;
}
*{box-sizing:border-box;margin:0;padding:0}
html,body{width:960px;height:1200px;overflow:hidden}
body{background:var(--paper);font-family:'Montserrat',sans-serif;color:var(--ink);position:relative}
.sheet{position:absolute;left:113px;width:735px;height:520px;display:flex;box-shadow:0 6px 18px rgba(0,0,0,.25)}
.sheet--outside{top:55px}
.sheet--inside{top:624px}
.panel{position:relative;width:245px;height:100%;overflow:hidden}
.panel--navy{background:var(--navy);color:var(--white);text-align:center}
.panel--white{background:var(--white)}
.photo{position:absolute;inset:0}
.photo--traveller{background:linear-gradient(170deg,#b9d6de 0%,#9cc0cc 35%,#c24a4f 55%,#3b6aa8 70%,#2d6a80 100%)}
.photo--suitcase{background:linear-gradient(160deg,#4fc9a6 0%,#3ab394 55%,#6f8a6a 80%,#3a3f3e 100%)}
.photo--station{background:linear-gradient(180deg,#cfcfcf 0%,#7a7a7a 55%,#b84040 80%,#4d4d4d 100%);height:171px;bottom:auto}
.photo--forest{background:linear-gradient(180deg,#d6d6d6 0%,#8c8c8c 50%,#3f5f9a 75%,#555 100%);height:171px;bottom:auto}
.brand{position:absolute;font-weight:800;color:var(--teal-dark);line-height:1;display:flex;align-items:center;gap:6px}
.brand__dot{width:12px;height:12px;border-radius:50%;background:var(--teal-dark)}
.brand--small{left:22px;top:28px;font-size:19px}
.brand--large{left:24px;top:48px;font-size:34px;flex-direction:column;align-items:flex-start;gap:4px}
.brand--large .brand__dot{width:18px;height:18px}
.stock-list{position:absolute;left:24px;top:160px;font-family:'Kaushan Script',cursive;color:var(--teal-dark);font-size:25px;line-height:1.35}
.tag{position:absolute;background:var(--yellow);color:var(--ink);text-align:center;font-weight:700}
.tag--price{left:14px;top:360px;width:219px;height:91px;padding-top:22px;font-size:22px;line-height:1.2}
.tag--delivery{left:34px;top:425px;width:187px;height:49px;line-height:49px;font-size:19px}
.promise{position:absolute;left:19px;top:467px;width:220px;color:var(--white);font-weight:700;font-size:13px;line-height:1.35}
.map{display:block;margin:22px auto 0;width:199px;height:120px;border-radius:6px;background:linear-gradient(135deg,#eef0f2,#dfe3e7)}
.map--second{margin-top:14px}
.store{margin-top:10px}
.store__name{font-weight:700;font-size:16.5px;letter-spacing:.2px}
.store__address{font-size:9.5px;margin-top:3px}
.store__phone{font-size:12.5px;margin-top:4px;font-weight:500}
.coupon{margin:12px auto 0;width:198px;height:62px;border:1.5px dashed rgba(255,255,255,.75);border-radius:8px;display:flex;align-items:center;padding:0 8px;gap:8px;text-align:left}
.coupon__save{color:var(--yellow);font-weight:800;font-size:25px;line-height:.95}
.coupon__save span{display:block;font-size:32px}
.coupon__lead{font-weight:700;font-size:10.5px;line-height:1.15}
.coupon__fine{font-weight:600;font-size:6px;line-height:1.3;margin-top:4px}
.coupon__fine em{font-style:normal;color:var(--yellow)}
.web{position:absolute;left:0;right:0;text-align:center;font-family:'Amatic SC',sans-serif;font-weight:700;font-size:20px;letter-spacing:.5px}
.web--light{bottom:4px;color:#7d8fab}
.web--teal{bottom:26px;color:var(--teal-dark)}
.photo-title{position:absolute;left:16px;top:118px;font-family:'Kaushan Script',cursive;font-size:38px;color:var(--white)}
.blurb{position:absolute;left:15px;right:14px;top:182px;font-size:13px;line-height:1.22;color:var(--ink)}
.logos{position:absolute;left:15px;right:12px;top:280px;display:flex;flex-wrap:wrap;gap:10px 12px;align-items:center;justify-content:center}
.partner{font-weight:700;font-size:14px;color:var(--ink);display:flex;align-items:center;gap:5px}
.partner__mark{width:11px;height:11px;background:var(--ink)}
.partner__mark--round{border-radius:50%;background:#d92b2b}
.partner--big{font-size:20px;font-weight:800}
.headline{margin-top:28px;font-weight:800;font-size:29px;line-height:1.05}
.headline__accent{color:var(--yellow)}
.subhead{font-weight:700;font-size:14px;margin-top:6px}
.body-copy{font-size:11.5px;line-height:1.3;margin:12px auto 0;width:200px}
.stamp{position:absolute;left:26px;top:222px;width:196px;height:50px;border:3px solid var(--yellow);transform:rotate(-12deg);color:var(--yellow);font-family:'Alfa Slab One',serif;font-size:15px;line-height:1.05;padding-top:8px;text-align:center}
.paylater{position:absolute;left:0;right:0;top:316px}
.paylater__name{font-weight:800;font-size:30px;line-height:1.1;display:flex;justify-content:center;align-items:center;gap:8px}
.paylater__name span{width:16px;height:16px;background:#39a935}
.paylater__title{font-weight:700;font-size:15.5px;margin-top:8px}
.paylater .body-copy{margin-top:6px}
.tag--returns{left:30px;top:450px;width:187px;height:46px;line-height:46px;font-size:17px}
</style>
</head>
<body>

<section class="sheet sheet--outside">
  <article class="panel panel--cover-left">
    <div class="photo photo--traveller" role="img" aria-label="Photo of a traveller from behind carrying a large red and blue backpack by the sea"></div>
    <div class="brand brand--small"><span class="brand__dot"></span>Moss Harbour</div>
    <div class="tag tag--price">BEST PRICE<br>Guarantee</div>
    <p class="promise">It's Simple. If you see a better price, we'll beat it on the spot</p>
  </article>

  <article class="panel panel--navy panel--stores">
    <div class="map" role="img" aria-label="Street map showing the Eastvale store location"></div>
    <div class="store">
      <div class="store__name">EASTVALE STORE</div>
      <div class="store__address">35 Calder Road, Eastvale,</div>
      <div class="store__phone">02 5550 1184</div>
    </div>
    <div class="map map--second" role="img" aria-label="Street map showing the Linfield store location"></div>
    <div class="store">
      <div class="store__name">LINFIELD STORE</div>
      <div class="store__address">Shop 2-325 Wren Street, Linfield</div>
      <div class="store__phone">02 5550 2283</div>
    </div>
    <div class="coupon">
      <div class="coupon__save">SAVE<span>30%</span></div>
      <div>
        <div class="coupon__lead">ON YOUR FIRST PURCHASE</div>
        <div class="coupon__fine">USE COUPON CODE <em>123456</em><br>OR CARRY THIS COUPON<br>TO THE STORE</div>
      </div>
    </div>
    <div class="web web--light">mossharbour.com.au</div>
  </article>

  <article class="panel panel--cover-front">
    <div class="photo photo--suitcase" role="img" aria-label="Photo of a hand holding a tan hat above a dark carry-on suitcase against a green wall"></div>
    <div class="brand brand--large"><span class="brand__dot"></span>MOSS<br>HARBOUR</div>
    <div class="stock-list">Luggage<br>Backpacks<br>Wallets<br>&amp; More</div>
    <div class="tag tag--delivery">Free Delivery</div>
  </article>
</section>

<section class="sheet sheet--inside">
  <article class="panel panel--white">
    <div class="photo photo--station" role="img" aria-label="Black and white photo of a traveller with a red suitcase on a train platform"></div>
    <div class="photo-title">Luggage</div>
    <p class="blurb">All the big brands at discount pricing - We select and stock a wide range of luggage, from low cost to premium luggage, all luggage is at least 40% OFF</p>
    <div class="logos">
      <div class="partner partner--big">VERANO</div>
      <div class="partner partner--big">Tandem</div>
      <div class="partner"><span class="partner__mark partner__mark--round"></span>Atlas Trek</div>
      <div class="partner">Kirra</div>
      <div class="partner"><span class="partner__mark partner__mark--round"></span>Bluegum</div>
      <div class="partner">Southern Bag Co.</div>
      <div class="partner"><span class="partner__mark"></span>Halden</div>
      <div class="partner">Nova Quest</div>
    </div>
    <div class="web web--teal">mossharbour.com.au</div>
  </article>

  <article class="panel panel--navy">
    <h1 class="headline"><span class="headline__accent">PRICE MATCH</span><br>GUARANTEED</h1>
    <div class="subhead">EVERY WEBSITE AND STORE</div>
    <p class="body-copy">We stock 1000's of big brand items, online and in our stores, if you see the same product somewhere else we will match the price on the spot.</p>
    <div class="stamp">NEVER BEATEN<br>ON PRICE</div>
    <div class="paylater">
      <div class="paylater__name"><span></span>PayLater Co</div>
      <div class="paylater__title">BUY NOW - PAY LATER</div>
      <p class="body-copy">We offer Layby and PayLater, giving you the option to Buy now and pay later and lock in the great deals on offer.</p>
    </div>
    <div class="tag tag--returns">30 DAY RETURNS</div>
  </article>

  <article class="panel panel--white">
    <div class="photo photo--forest" role="img" aria-label="Black and white photo of a hiker with a blue backpack walking through woodland"></div>
    <div class="photo-title">Backpacks</div>
    <p class="blurb">We stock a wide range of brands and styles, from the latest fashion backpacks to the practical work bags and messengers - All at market leading prices.</p>
    <div class="logos">
      <div class="partner"><span class="partner__mark partner__mark--round"></span>Bluegum</div>
      <div class="partner partner--big">DRIZZLE</div>
      <div class="partner partner--big">Fernvik</div>
      <div class="partner"><span class="partner__mark"></span>Coralpath</div>
      <div class="partner">Wrenly</div>
      <div class="partner">Slimcard</div>
      <div class="partner"><span class="partner__mark"></span>Marlowe</div>
    </div>
    <div class="web web--teal">mossharbour.com.au</div>
  </article>
</section>

</body>
</html>
```